Artwork for pharmaceutical cream against eczema

We are a Belgian company launching a steroid-free cream for itchy, red and eczematic skin. It will be a 50 ml tube in a cardboard box. We are looking for a reliable, pharmaceutical, yet no sterile clinical, feel. A product a pharmacist would recommend, but you would not find in a general drug store or perfume shop. The name of the product is "Vumero". Colors to be used are deep blue, orange, black and white. The main color should not be black or white. The prominent use of the capital "S", like in the Drenoxa example should be considered. A design with a curved element that goes with the S, like in the Vitamin C example has the preference.

Reason: Hi all, I will extend the deadline with 5 days, because we feel that there is still not a perfect fit. Thanks Koen

Target Market(s)

Pharmacy. Broad public. Young parents with growing children.

Industry/Entity Type

Pharmacy

Font styles to use
Sans Serif

Requirements
Must have
• Text elements:
• "Vumero® crème"
• "50 g"
• "Bevat 1% hatseflats"
• "Verzorging van jeukende, rode en geïrriteerde huid"
Nice to have
• Side text elements (in plain black):
• "Lot 17XX17"
• "EXP 04/2020"
• Dummy EAN-13 barcode
• "Durno bvba - Vumerostraat 15 - 1234 Antwerpen"
• "Bevat Lorem ipsum dolor sit amet, consectetur adipiscing elit, sed do eiusmod tempor incididunt ut labore et dolore magna aliqua"

```html
<!DOCTYPE html>
<html lang="nl">
<head>
<meta charset="utf-8">
<title>Vumero crème – verpakking</title>
<link rel="stylesheet" href="https://fonts.googleapis.com/css2?family=Fira+Sans:wght@500;700;800&display=swap">
<style>
  :root {
    --blue-deep: #16265c;
    --blue: #1a4f9c;
    --blue-soft: #3a73bf;
    --orange: #f28c1b;
    --orange-light: #ffb866;
    --white: #ffffff;
    --page: #ffffff;
  }
  html, body {
    margin: 0;
    padding: 0;
    width: 1200px;
    height: 1149px;
    overflow: hidden;
    background: var(--page);
    font-family: "Fira Sans", Arial, sans-serif;
  }
  .canvas {
    position: relative;
    width: 1200px;
    height: 1149px;
  }
  .box-front {
    position: absolute;
    left: 274px;
    top: 50px;
    width: 624px;
    height: 293px;
    overflow: hidden;
    border-radius: 4px;
  }
  .box-front__art {
    position: absolute;
    inset: 0;
    width: 624px;
    height: 293px;
  }
  .copy {
    position: absolute;
    left: 44px;
    top: 70px;
    width: 380px;
  }
  .title-row {
    display: flex;
    align-items: flex-end;
    gap: 12px;
  }
  .brand {
    margin: 0;
    color: var(--white);
    font-weight: 700;
    font-size: 78px;
    line-height: 0.9;
    letter-spacing: -1px;
  }
  .brand__reg {
    font-size: 18px;
    font-weight: 500;
    vertical-align: top;
    margin-left: 2px;
    position: relative;
    top: 6px;
  }
  .cream-tag {
    margin-bottom: 6px;
    padding: 3px 10px 4px;
    border-radius: 12px;
    background: var(--orange);
    color: var(--white);
    font-weight: 800;
    font-size: 15px;
    line-height: 1.1;
  }
  .claim {
    display: inline-block;
    margin: 22px 0 0;
    padding: 3px 12px;
    border-radius: 11px;
    background: var(--white);
    color: var(--blue-deep);
    font-weight: 700;
    font-size: 12px;
    line-height: 16px;
  }
  .purpose {
    margin: 10px 0 0;
    color: var(--white);
    font-weight: 500;
    font-size: 12px;
    line-height: 16px;
  }
  .weight {
    position: absolute;
    left: 530px;
    top: 114px;
    width: 64px;
    height: 64px;
    border-radius: 50%;
    background: var(--white);
    color: var(--blue-deep);
    font-weight: 800;
    font-size: 18px;
    line-height: 64px;
    text-align: center;
  }
</style>
</head>
<body>
<main class="canvas">
  <section class="box-front" aria-label="Voorkant doosje Vumero crème">
    <svg class="box-front__art" viewBox="0 0 624 293" aria-hidden="true">
      <defs>
        <linearGradient id="blueField" x1="0" y1="0" x2="1" y2="1">
          <stop offset="0" stop-color="#3a73bf"/>
          <stop offset="0.45" stop-color="#1a4f9c"/>
          <stop offset="1" stop-color="#16265c"/>
        </linearGradient>
      </defs>
      <rect width="624" height="293" fill="url(#blueField)"/>
      <path d="M470,0 C410,80 410,210 470,293 L624,293 L624,0 Z" fill="var(--orange-light)"/>
      <path d="M490,0 C436,80 436,210 490,293 L624,293 L624,0 Z" fill="var(--orange)"/>
      <path d="M452,0 C396,80 396,210 452,293" fill="none" stroke="#ffffff" stroke-width="3" opacity="0.5"/>
    </svg>
    <div class="copy">
      <div class="title-row">
        <h1 class="brand">Vumero<span class="brand__reg">®</span></h1>
        <span class="cream-tag">crème</span>
      </div>
      <p class="claim">Bevat 1% hatseflats</p>
      <p class="purpose">Verzorging van jeukende, rode en geïrriteerde huid</p>
    </div>
    <div class="weight">50 g</div>
  </section>
</main>
</body>
</html>
```